Service Plan Sales Flyer

The Watchpost Depot (www.kelvamart.com) is a commercial security integrator that installs security cameras, access control, intrusion, two-way radios and perimeter security. We require a one page flyer for our service plan for new and existing customers. The price of the service plan is $299/yr and includes the following;
1. Discounted service rate of $118/hr
2. Free remote support ($85/hr without a plan)
3. Free remote training
4. Priority support

Please review our brochure attached and create a one page sales flyer with the end goal of having the client sign up for our annual service plan . The plan will automatically renew every year. Email sales@kelvamart.com.

Target Market(s)

commercial industrial clients - no residential

Industry/Entity Type

review our website at www.kelvamart.com

Colors
0054AA
0677BA
7BADD7
CADEEF
E8F1F8
EE7325
F08F49
F5BC92
FAE3D3
FDF4ED

Requirements
Must have
• call to action
Should not have
• too many colors

```html
<!DOCTYPE html>
<html lang="en">
<head>
<meta charset="utf-8">
<title>Service Plan Flyer – The Watchpost Depot</title>
<link href="https://fonts.googleapis.com/css2?family=Red+Hat+Display:wght@300;400;500;700;900&display=swap" rel="stylesheet">
<style>
  :root {
    --red: #ee4237;
    --navy: #1b2f5b;
    --white: #ffffff;
    --stage: #ececec;
    --text: #1b2f5b;
  }
  * { margin: 0; padding: 0; box-sizing: border-box; }
  html, body { width: 1200px; height: 1200px; overflow: hidden; }
  body { background: var(--stage); font-family: "Red Hat Display", sans-serif; color: var(--text); }

  .flyer { position: absolute; left: 175px; top: 0; width: 850px; height: 1200px; background: var(--white); overflow: hidden; }

  .hero-swoosh { position: absolute; left: 0; top: 0; width: 850px; height: 400px; }

  .brand { position: absolute; left: 60px; top: 80px; display: flex; align-items: center; gap: 9px; z-index: 2; }
  .brand-mark { width: 20px; height: 20px; background: var(--navy); flex: none; }
  .brand-name { font-size: 21px; font-weight: 900; color: var(--navy); white-space: nowrap; }

  .product-visual { position: absolute; left: 352px; top: 74px; width: 376px; height: 255px; border-radius: 10px;
    background: linear-gradient(160deg, #f4f4f5 0%, #dcdde0 55%, #bfc3c9 100%); }

  .price-badge { position: absolute; left: 669px; top: 328px; width: 166px; height: 166px; border-radius: 50%;
    background: var(--red); border: 8px solid var(--navy); box-shadow: 0 8px 14px rgba(0,0,0,0.25);
    display: flex; flex-direction: column; align-items: center; justify-content: center; color: var(--white); font-weight: 900; }
  .price-label { font-size: 23px; line-height: 1.2; }
  .price-value { font-size: 22px; line-height: 1.3; }

  .headline { position: absolute; left: 50px; top: 405px; }
  .headline-lead { font-size: 23px; font-weight: 400; line-height: 26px; color: var(--navy); letter-spacing: 0.5px; }
  .headline-main { font-size: 46px; font-weight: 900; color: var(--red); line-height: 1.05; letter-spacing: 0.5px; }

  .band { position: absolute; height: 37px; color: var(--white); font-size: 23px; font-weight: 900; display: flex; align-items: center; white-space: nowrap; }
  .band-red { left: 0; width: 449px; background: var(--red); clip-path: polygon(0 0, 100% 0, 91.3% 100%, 0 100%); padding-left: 50px; }
  .band-navy { left: 477px; width: 373px; background: var(--navy); clip-path: polygon(0 0, 100% 0, 100% 100%, 11.3% 100%); justify-content: flex-end; padding-right: 50px; }

  .feature-copy { position: absolute; width: 336px; font-size: 16px; line-height: 19px; font-weight: 400; color: var(--navy); letter-spacing: 0.45px; }
  .copy-left { left: 50px; }
  .copy-right { left: 464px; text-align: right; }

  .rate { position: absolute; font-size: 22px; font-weight: 900; color: var(--red); text-align: right; width: 200px; left: 144px; }

  .cta { position: absolute; left: 0; top: 1018px; width: 850px; height: 71px; background: var(--red); text-align: center; }
  .cta-title { font-size: 24px; font-weight: 900; color: var(--navy); line-height: 34px; padding-top: 3px; letter-spacing: 0.3px; }
  .cta-url { font-size: 26px; font-weight: 500; color: var(--white); line-height: 30px; }

  .note { position: absolute; left: 0; top: 1123px; width: 850px; text-align: center; font-size: 22px; font-weight: 500; color: var(--navy); }
  .note-label { color: var(--red); font-weight: 900; }
</style>
</head>
<body>
  <main class="flyer">
    <svg class="hero-swoosh" viewBox="0 0 850 400" aria-hidden="true">
      <defs>
        <linearGradient id="hero-fill" x1="0" y1="0" x2="0" y2="1">
          <stop offset="0" stop-color="#ffffff"/>
          <stop offset="0.6" stop-color="#f7f7f7"/>
          <stop offset="1" stop-color="#e4e4e5"/>
        </linearGradient>
      </defs>
      <path d="M0,0 L0,123 Q425,647 850,123 L850,0 Z" fill="var(--red)"/>
      <path d="M0,0 L0,110 Q425,626 850,110 L850,0 Z" fill="var(--navy)"/>
      <path d="M0,0 L0,100 Q425,594 850,100 L850,0 Z" fill="url(#hero-fill)"/>
    </svg>

    <div class="brand">
      <span class="brand-mark"></span>
      <span class="brand-name">The Watchpost Depot</span>
    </div>

    <div class="product-visual" role="img" aria-label="Security products: a door with access control reader, a monitor showing camera footage, a dome camera and a bullet camera"></div>

    <div class="price-badge">
      <span class="price-label">PRICE:</span>
      <span class="price-value">$299 | year</span>
    </div>

    <header class="headline">
      <p class="headline-lead">SECURE YOUR BUSINESS<br>WITH OUR COMPREHENSIVE</p>
      <h1 class="headline-main">SERVICE PLAN</h1>
    </header>

    <h2 class="band band-red" style="top:556px;">Discounted Service Rate:</h2>
    <h2 class="band band-navy" style="top:556px;">Free Remote Training:</h2>

    <p class="feature-copy copy-left" style="top:605px;">Receive a discounted service rate of $118/hour for any security-related services provided by The Watchpost Depot. This reduced rate ensures cost-effective support and maintenance for your security systems.</p>
    <p class="rate" style="top:722px;">$118 per hour</p>

    <p class="feature-copy copy-right" style="top:605px;">Take advantage of our complimentary remote training sessions. Our experienced trainers will guide you through the operation and management of your security systems, ensuring you have the knowledge and confidence to utilize them effectively.</p>

    <h2 class="band band-red" style="top:767px;">Free Remote Support:</h2>
    <h2 class="band band-navy" style="top:767px;">Priority Support:</h2>

    <p class="feature-copy copy-left" style="top:818px;">Enjoy free remote support from our expert technicians. Our team will assist you remotely with any technical issues or questions you may have regarding your security systems. Without a service plan, remote support is billed at $85/hour, so this benefit saves you money.</p>
    <p class="rate" style="top:968px;">$85 per hour</p>

    <p class="feature-copy copy-right" style="top:818px;">As a service plan subscriber, you will receive priority support. Your inquiries and requests will be given expedited attention, ensuring prompt assistance and minimizing any downtime or disruptions to your security systems.</p>

    <section class="cta">
      <p class="cta-title">GET STARTED WITH OUR SERVICE PLAN NOW</p>
      <p class="cta-url">www.kelvamart.com</p>
    </section>

    <p class="note"><span class="note-label">NOTE:</span> The plan will automatically renew every year</p>
  </main>
</body>
</html>
```